Dozing Heron

Need a business card for our restaurant. Restaurant and Bar in the mountains of North Idaho. Rustic looking card

Contact Information for Business Card

rustic design, wood and metal looking, primarily neutral colors

Requirements
Must have
• Name, address, phone number, website, email address

```html
<!DOCTYPE html>
<html lang="en">
<head>
<meta charset="utf-8">
<title>Dozing Heron – Business Card</title>
<link href="https://fonts.googleapis.com/css2?family=Montserrat:wght@400;500;700&display=swap" rel="stylesheet">
<style>
  :root{
    --page:#2a2826;
    --card-white:#ffffff;
    --card-black:#111111;
    --ink:#141414;
    --ink-soft:#4a4a4a;
    --pattern-light:#6a6a6a;
    --pattern-dark:#1c1c1c;
    --on-dark:#f4f4f4;
  }
  *{box-sizing:border-box;margin:0;padding:0}
  html,body{width:1200px;height:900px;overflow:hidden}
  body{
    background:var(--page);
    font-family:"Montserrat",sans-serif;
    position:relative;
  }
  .card{
    position:absolute;
    width:540px;height:309px;
    border-radius:26px;
    overflow:hidden;
    box-shadow:0 14px 30px rgba(0,0,0,.45);
  }
  /* back side */
  .card-back{left:40px;top:295px;background:var(--card-black)}
  .card-back .pattern{
    position:absolute;inset:0;
    background:linear-gradient(135deg,var(--pattern-light) 0%,#3a3a3a 38%,var(--pattern-dark) 70%,#0c0c0c 100%);
  }
  .card-back .brand{
    position:absolute;left:50%;top:50%;transform:translate(-50%,-50%);
    display:flex;align-items:center;gap:12px;
    background:var(--card-black);
    padding:16px 22px;border-radius:60px;
  }
  .card-back .brand-dot{width:16px;height:16px;border-radius:50%;background:var(--on-dark)}
  .card-back .brand-name{
    color:var(--on-dark);font-weight:500;font-size:19px;letter-spacing:.14em;text-transform:uppercase;
  }
  /* front side */
  .card-front{left:620px;top:295px;background:var(--card-white);color:var(--ink)}
  .card-front .brand{
    position:absolute;right:40px;top:36px;
    display:flex;align-items:center;gap:10px;
  }
  .card-front .brand-dot{width:16px;height:16px;border-radius:50%;background:var(--ink)}
  .card-front .brand-name{
    font-weight:500;font-size:17px;letter-spacing:.14em;text-transform:uppercase;color:var(--ink);
  }
  .identity{position:absolute;left:40px;top:116px}
  .identity .person-name{font-weight:700;font-size:27px;letter-spacing:.01em}
  .identity .person-role{font-size:14px;color:var(--ink-soft);margin-top:4px}
  .divider{position:absolute;left:262px;top:168px;width:2px;height:66px;background:var(--ink)}
  .contacts{position:absolute;left:282px;top:166px;list-style:none;font-size:15px;color:var(--ink-soft)}
  .contacts li{display:flex;align-items:center;gap:9px;height:24px}
  .contacts svg{width:13px;height:13px;fill:var(--ink)}
  .address{position:absolute;left:40px;top:256px;font-size:14.5px;color:var(--ink-soft)}
</style>
</head>
<body>

<section class="card card-back" aria-label="Card back">
  <div class="pattern" role="img" aria-label="Repeating brand emblem pattern in glossy grey and black"></div>
  <div class="brand">
    <span class="brand-dot"></span>
    <span class="brand-name">The Dozing Heron</span>
  </div>
</section>

<section class="card card-front" aria-label="Card front">
  <div class="brand">
    <span class="brand-dot"></span>
    <span class="brand-name">The Dozing Heron</span>
  </div>

  <div class="identity">
    <h1 class="person-name">Owen Harlan</h1>
    <p class="person-role">Managing Director</p>
  </div>

  <div class="divider"></div>

  <ul class="contacts">
    <li>
      <svg viewBox="0 0 24 24" aria-hidden="true"><path d="M6.6 10.8a15.1 15.1 0 0 0 6.6 6.6l2.2-2.2c.3-.3.7-.4 1-.2 1.1.4 2.3.6 3.6.6.6 0 1 .4 1 1V20c0 .6-.4 1-1 1A17 17 0 0 1 3 4c0-.6.4-1 1-1h3.5c.6 0 1 .4 1 1 0 1.3.2 2.5.6 3.6.1.3 0 .7-.2 1z"/></svg>
      <span>123 456 789</span>
    </li>
    <li>
      <svg viewBox="0 0 24 24" aria-hidden="true"><path d="M2 5h20v14H2zM3.5 6.5v.6L12 13l8.5-5.9v-.6z"/></svg>
      <span>info@yourgmail.com</span>
    </li>
    <li>
      <svg viewBox="0 0 24 24" aria-hidden="true"><circle cx="12" cy="12" r="10"/></svg>
      <span>www.yourwebsite.com</span>
    </li>
  </ul>

  <p class="address">Your address, City State, Zip 1234</p>
</section>

</body>
</html>
```